Looking for a new business card design

We are looking for a corporate looking yet still a bit different then the rest. I would like the card black with the picture on the back and the phrase "Guiding every crew to zero harm" on the back as well. Then a clean look on the front with a bit of an edge.

Target Market(s)

Corporate oil executives and drilling supervisors

Industry/Entity Type

Oil And Gas

Contact Information for Business Card

Black, bold, clean lines.

Font styles to use
Sans Serif

Requirements
Must have
• Picture on the back with the slogan "Guiding every crew to zero harm"
• Black background
• Stands out

```html
<!DOCTYPE html>
<html lang="en">
<head>
<meta charset="utf-8">
<title>Trevalon Energy Services Corp – Business Card</title>
<link href="https://fonts.googleapis.com/css2?family=Montserrat:wght@400;500;700&display=swap" rel="stylesheet">
<style>
  :root {
    --page-bg: #e4e2de;
    --card-black: #1b1b1b;
    --card-black-deep: #121212;
    --band-black: #1d1d1d;
    --accent-green: #b8cc2f;
    --text-white: #f2f2f2;
    --site-dark: #0c0d0b;
    --site-ground: #8a7f62;
    --site-light: #d9d3bd;
  }
  * { margin: 0; padding: 0; box-sizing: border-box; }
  html, body {
    width: 1200px; height: 1000px; overflow: hidden;
    background: var(--page-bg);
    font-family: "Montserrat", Arial, sans-serif;
  }
  .canvas { position: relative; width: 1200px; height: 1000px; }

  .card {
    position: absolute; left: 266px; width: 666px; height: 396px;
    overflow: hidden;
    box-shadow: 0 3px 10px rgba(0,0,0,0.25);
  }
  .card-front {
    top: 75px;
    background: linear-gradient(135deg, var(--card-black) 0%, var(--card-black-deep) 100%);
    color: var(--text-white);
  }
  .card-back { top: 534px; background: var(--site-dark); }

  /* Front */
  .brand { position: absolute; left: 38px; top: 80px; color: var(--accent-green); font-weight: 500; }
  .brand-name { font-size: 40px; line-height: 1; letter-spacing: 0.3px; }
  .brand-sub { font-size: 16px; line-height: 1.3; margin-top: 4px; }

  .person { position: absolute; right: 38px; top: 90px; text-align: right; }
  .person-name { color: var(--accent-green); font-weight: 700; font-size: 19px; letter-spacing: 0.3px; }
  .person-title { font-size: 14.5px; margin-top: 4px; }

  .address { position: absolute; left: 38px; top: 215px; font-size: 14.5px; line-height: 24px; }

  .contacts { position: absolute; left: 38px; top: 282px; list-style: none; font-size: 14.5px; }
  .contacts li { display: flex; align-items: center; height: 24.5px; }
  .contacts svg { width: 14px; height: 14px; margin-right: 8px; fill: var(--accent-green); }

  /* Back */
  .site-photo {
    position: absolute; inset: 0;
    background:
      radial-gradient(ellipse 45% 38% at 42% 30%, rgba(255,255,255,0.55), transparent 70%),
      radial-gradient(ellipse 60% 55% at 50% 48%, var(--site-light) 0%, var(--site-ground) 45%, #3c382b 75%, var(--site-dark) 100%);
  }
  .slogan-band {
    position: absolute; left: 0; right: 0; top: 296px; height: 66px;
    background: var(--band-black);
    display: flex; align-items: center; justify-content: space-between;
    padding: 0 32px;
  }
  .slogan { color: var(--text-white); font-size: 19px; font-weight: 400; }
  .band-brand { color: var(--accent-green); font-weight: 500; text-align: left; }
  .band-brand .brand-name { font-size: 24px; }
  .band-brand .brand-sub { font-size: 10px; margin-top: 2px; }
</style>
</head>
<body>
<div class="canvas">

  <section class="card card-front">
    <div class="brand">
      <div class="brand-name">TREVALON</div>
      <div class="brand-sub">Energy Services Corp</div>
    </div>

    <div class="person">
      <div class="person-name">DARA WHITLOCK</div>
      <div class="person-title">Executive Director</div>
    </div>

    <div class="address">
      Post Office Box 4410387<br>
      Lake Charles, LA 70612
    </div>

    <ul class="contacts">
      <li>
        <svg viewBox="0 0 16 16" aria-hidden="true"><path d="M2 5c0-2 1-3 6-3s6 1 6 3v1h-3V5H5v1H2zM4 7h8l2 7H2z"/></svg>
        + 000 000 0000 EXT 1
      </li>
      <li>
        <svg viewBox="0 0 16 16" aria-hidden="true"><path d="M1 3h14v10H1z M1.5 3.5 8 9l6.5-5.5" stroke="#1b1b1b" stroke-width="1.2"/></svg>
        info@TrevalonEnergy.com
      </li>
      <li>
        <svg viewBox="0 0 16 16" aria-hidden="true"><circle cx="8" cy="8" r="7"/><path d="M1 8h14M8 1c-3 3-3 11 0 14M8 1c3 3 3 11 0 14" stroke="#1b1b1b" stroke-width="1.1" fill="none"/></svg>
        www.TrevalonEnergy.com
      </li>
    </ul>
  </section>

  <section class="card card-back">
    <div class="site-photo" role="img" aria-label="Aerial night photograph of a brightly lit drilling rig site with equipment and trailers on a sandy pad surrounded by dark trees"></div>
    <div class="slogan-band">
      <p class="slogan">Guiding every crew to zero harm</p>
      <div class="band-brand">
        <div class="brand-name">TREVALON</div>
        <div class="brand-sub">Energy Services Corp</div>
      </div>
    </div>
  </section>

</div>
</body>
</html>
```